Exclusive British Dental Clinic Needs Modern Brochure to Attract New Patients

We are looking to create a smart, sophisticated brochure that gives the public and future potential clients a concise overview of what we offer and why the quality and care on offer is a step above the rest. We are based in the United Kingdom where the Public Wellness Board provide dental care free or at low cost. We are NOT an PWB provider. We are a wholly private dental clinic so all of our patients are paying full-price premium prices directly out of pocket. The work we do is exceptional so all of our patients can be assured that anything we do is done to the highest and best quality possible.
We offer high quality dental treatment using the best and latest techniques, materials and an award winning dental laboratory. All treatments are undertaken using high quality magnification to ensure the best possible result. We have over 30 years’ experience in general dentistry with fully trained staff. In quality comfortable surroundings, we are a caring practice with excellent patient care. We allow more time with our patients and we understand and care for nervous patients.
We also offer facial fillers, wrinkle reducers and teeth whitening in order to help our patients achieve their best look.

We have attached our logo and logo icons to this brief.
We also have attached some information in our Brochure Details document. This just highlights what we would like to see and more information about us.
We are really up to suggestion with design and wording because we want this brochure to be attractive and appealing to the public.
Feel free to edit as you see fit to help us attain our goals :)

Reason: Hello We are very excited about the work we have received thus far...our Practice Manager is away for the next week and we wanted to make sure we are all on board for the discussions and decisions we make moving forward. Thank you for taking the time to help us create our voice! --- Larkmoor Atelier Dental Clinic

```html
<!DOCTYPE html>
<html lang="en">
<head>
<meta charset="utf-8">
<title>Cosmetic Dentistry Brochure – Inside Spread</title>
<link href="https://fonts.googleapis.com/css2?family=Source+Sans+3:wght@300;400;600;700&display=swap" rel="stylesheet">
<style>
  :root {
    --page-bg: #e4e4e6;
    --paper: #ffffff;
    --ink: #3d3d3f;
    --ink-soft: #4a4a4c;
    --brand-blue: #0a8fd6;
    --photo-light: #f3ebe3;
    --photo-warm: #e2cdbb;
  }
  * { margin: 0; padding: 0; box-sizing: border-box; }
  html, body {
    width: 1200px; height: 900px; overflow: hidden;
    background: var(--page-bg);
    font-family: "Source Sans 3", "Source Sans Pro", Arial, sans-serif;
    color: var(--ink);
  }
  .spread {
    position: absolute; left: 35px; top: 10px;
    width: 904px; height: 703px;
    transform: scale(1.25); transform-origin: 0 0;
    background: var(--paper);
    overflow: hidden;
  }
  .panel { position: absolute; z-index: 3; }
  .panel-title {
    font-weight: 300; font-size: 27px; line-height: 1;
    color: var(--ink-soft);
  }
  /* Left panel */
  .panel-services { left: 34px; width: 236px; top: 37px; }
  .services-intro {
    margin-top: 9px; font-size: 15px; line-height: 17.7px;
    font-weight: 400; text-align: justify;
  }
  .services-label { margin-top: 17px; font-size: 15px; font-weight: 300; line-height: 17.7px; }
  .services-list { list-style: none; margin-left: 10px; }
  .services-list li {
    position: relative; padding-left: 8px;
    font-size: 14.6px; font-weight: 600; line-height: 17.6px;
  }
  .services-list li::before {
    content: ""; position: absolute; left: 0; top: 7px;
    width: 5px; height: 5px; border-radius: 1px; background: var(--brand-blue);
  }
  /* Middle panel */
  .panel-prices { left: 329px; width: 236px; top: 37px; }
  .price-group { margin-top: 8px; font-size: 13.6px; line-height: 16.4px; font-weight: 400; }
  .price-group + .price-group { margin-top: 16px; }
  .price-note {
    margin-top: 8px; font-size: 8.6px; line-height: 9.6px; font-weight: 600;
    text-align: justify;
  }
  /* Right panel */
  .panel-faqs { left: 630px; width: 236px; top: 34px; }
  .faq-list { margin-top: 9px; }
  .faq-item { margin-bottom: 10px; }
  .faq-question { font-size: 10.4px; line-height: 12.4px; font-weight: 700; }
  .faq-answer { font-size: 9.6px; line-height: 12.1px; font-weight: 400; text-align: justify; }
  /* Visual layers */
  .hero-photo {
    position: absolute; left: 104px; top: 318px; width: 440px; height: 330px;
    background: linear-gradient(180deg, var(--photo-light) 0%, var(--photo-warm) 100%);
    z-index: 1;
  }
  .wave { position: absolute; left: 0; top: 0; width: 904px; height: 703px; z-index: 2; }
</style>
</head>
<body>
  <main class="spread">
    <div class="hero-photo" role="img" aria-label="Photograph of a smiling young couple embracing, showing bright white teeth"></div>

    <svg class="wave" viewBox="0 0 904 703" aria-hidden="true">
      <defs>
        <linearGradient id="waveLight" x1="0" y1="0" x2="1" y2="0">
          <stop offset="0" stop-color="#8ec7ea"/>
          <stop offset="0.5" stop-color="#3fb0e8"/>
          <stop offset="1" stop-color="#14a5e6"/>
        </linearGradient>
        <linearGradient id="waveDeep" x1="0" y1="0" x2="0" y2="1">
          <stop offset="0" stop-color="#1a9ce0"/>
          <stop offset="1" stop-color="#0a8fd6"/>
        </linearGradient>
      </defs>
      <path d="M0,328 C50,500 250,652 560,663 C700,668 820,652 904,638 L904,703 L0,703 Z" fill="url(#waveLight)"/>
      <path d="M0,372 C70,540 280,652 600,664 C720,668 830,656 904,646 L904,703 L0,703 Z" fill="url(#waveDeep)"/>
    </svg>

    <section class="panel panel-services">
      <h2 class="panel-title">Cosmetic Dentistry</h2>
      <p class="services-intro">We offer a full range of treatment options in cosmetic dentistry and facial cosmetic rejuvenation. Looking good often translates into feeling good.</p>
      <p class="services-label">Treatments Include:</p>
      <ul class="services-list">
        <li>Whitening</li>
        <li>Veneers</li>
        <li>Tooth Coloured Fillings</li>
        <li>Crowns</li>
        <li>Wrinkle Reducers</li>
        <li>Facial Fillers</li>
        <li>Lip Enhancement</li>
      </ul>
    </section>

    <section class="panel panel-prices">
      <h2 class="panel-title">Treatment Prices</h2>
      <div class="price-group">
        <p>New Patient Examination and Consultation<br>- £150.00</p>
        <p>Routine Examination - £70.00</p>
        <p>Hygienist Visit – from £75.00</p>
        <p>Fillings – from £150.00</p>
        <p>Veneers – from £725.00</p>
        <p>Crowns – from £775.00</p>
      </div>
      <div class="price-group">
        <p>Whitening – from £399.00</p>
        <p>Wrinkle Reducers – from £225.00</p>
        <p>Facial Fillers&nbsp; – from £275.00</p>
        <p>Lip Enhancement – from £295.00</p>
      </div>
      <p class="price-note">*All treatments are carried out under optical magnification systems for improved accuracy. We are a mercury free practice*</p>
    </section>

    <section class="panel panel-faqs">
      <h2 class="panel-title">FAQs</h2>
      <div class="faq-list">
        <div class="faq-item">
          <p class="faq-question">What is involved in an initial consultation?</p>
          <p class="faq-answer">We believe this is the most important appointment. Each patient is an individual and An initial consultation consists of a full examination of all hard and soft tissue, an oral cancer screening, and periodontal examination as well as any necessary radiographs, photographs and/or special tests.</p>
        </div>
        <div class="faq-item">
          <p class="faq-question">How often should I see the dentist?</p>
          <p class="faq-answer">We recommend a six-monthly visit to both the dentist and hygienist to keep your teeth in optimum health. Research shows that a visit to the dentist every 6 months will help to prevent gum disease, cavities and the need for extensive dental treatment.</p>
        </div>
        <div class="faq-item">
          <p class="faq-question">Why should I choose private dental care?</p>
          <p class="faq-answer">Private treatment offers a broad range of general and cosmetic dentistry with the aim of creating a smile you are happy with, attractive confident. waiting time is considerably less, but our attention to detail and time spent on each appointment is greater as we are not worried about targets so we can give you more attention and time during treatment. range of treatment</p>
        </div>
        <div class="faq-item">
          <p class="faq-question">What happens during a scale and polish?</p>
          <p class="faq-answer">Think of a ‘scale’ as a powerwash for your teeth. Brushing can only get rid of surface plaque but scaling gets rid of hard formed tartar; Polishing helps to remove surface staining.</p>
        </div>
        <div class="faq-item">
          <p class="faq-question">Is teeth whitening safe?</p>
          <p class="faq-answer">Yes. Clinical studies have shown that whitening your teeth with carbamide or hydrogen peroxide under the supervision of a dental professional is safe for teeth and gums.&nbsp; All of our whitening options are EU compliant</p>
        </div>
        <div class="faq-item">
          <p class="faq-question">What are facial fillers and will they correct my wrinkles?</p>
          <p class="faq-answer">Facial fillers are compromised of injectable hyaluronic acid, which can hold 2000 times its weight in moisture. They improve the appearance of fine lines and wrinkles, but may not completely correct. Each experience varies by individual. We offer a complete consultation prior to carrying out treatment where the best options for you will be discussed.</p>
        </div>
      </div>
    </section>
  </main>
</body>
</html>
```